Maple Cove Laser Dermal Studio needs an 8 page WP redesign

We need a colorful re-design for an 8 page Wordpress website. The current preliminary website is live. The home page URL is http://maplecovelaserdermalstudio.com The new logo is live on the website also. I would like a (re)design using the colors that are represented by the new logo file, and any additional complimentary colors. The information regarding the business can be found on the website already, so please review it for insight. The name of the business is "Maple Cove Laser Dermal Studio".

Target Market(s)

The targeted website viewer is an adult female between the ages of 30 and 75 who is interested in facial renewal, wart removal and scar removal. This website should inspire in the target viewer the benefits of laser facial renewal, wart removal and new scar removal. Potential website viewers are wanting and searching for improved skin health and appearance. The website must represent the essence of a professional spa business.

Industry/Entity Type

Business

Font styles to use
Sans Serif

Requirements
Must have
• - The phone number placed in a visible and high value widget area that allows mobile phone browser dialing.

```html
<!DOCTYPE html>
<html lang="en">
<head>
<meta charset="utf-8">
<title>Maple Cove Laser Dermal Studio</title>
<link href="https://fonts.googleapis.com/css2?family=Raleway:wght@400;500;600&family=Open+Sans:wght@400;600&display=swap" rel="stylesheet">
<style>
:root{
  --plum-dark:#1c0d1c;
  --plum:#3d1f3b;
  --magenta:#b52fb5;
  --magenta-light:#cf48cf;
  --magenta-deep:#951d95;
  --wine:#5a1450;
  --ink:#2d2d2d;
  --text:#6a6a6a;
  --line:#e2e2e2;
  --white:#ffffff;
}
*{margin:0;padding:0;box-sizing:border-box}
html,body{width:910px;height:1200px;overflow:hidden;background:var(--white)}
body{position:relative;font-family:'Open Sans',sans-serif;color:var(--text)}
.abs{position:absolute}
.header-band{left:0;top:0;width:910px;height:235px;background:linear-gradient(180deg,var(--plum) 0%,var(--plum-dark) 100%)}
.brand{left:120px;top:34px;color:var(--white);font-family:'Raleway',sans-serif;font-weight:600;font-size:17px;line-height:20px;display:flex;align-items:center;gap:8px}
.brand-dot{width:30px;height:30px;border-radius:50%;background:var(--magenta)}
.call{right:125px;top:45px;text-align:right;font-family:'Raleway',sans-serif}
.call-label{color:var(--magenta-light);font-size:10px}
.call-number{color:var(--white);font-size:16px;display:flex;align-items:center;gap:5px;text-decoration:none}
.main-nav{left:120px;top:86px;width:670px;height:32px;background:linear-gradient(180deg,var(--magenta-light),var(--magenta-deep));display:flex;padding-left:2px}
.main-nav a{color:var(--white);text-decoration:none;font-family:'Raleway',sans-serif;font-weight:600;font-size:10px;line-height:32px;padding:0 14px;border-right:1px solid rgba(255,255,255,.25)}
.main-nav a:last-child{border-right:0}
.hero{left:120px;top:118px;width:670px;height:276px;background:linear-gradient(90deg,#f7f7f7 0%,#eef0ef 45%,#cdd6d3 70%,#b6c2bf 100%);border:1px solid var(--line);box-shadow:0 6px 12px rgba(0,0,0,.08)}
.hero-copy{left:40px;top:86px;width:260px}
.hero-title{font-family:'Raleway',sans-serif;font-size:25px;font-weight:500;color:#4b2c47}
.hero-sub{font-family:'Raleway',sans-serif;font-size:13px;color:var(--magenta);margin-top:2px}
.hero-body{font-size:8px;line-height:13px;margin-top:6px}
.hero-dots{display:flex;gap:3px;margin-top:12px}
.hero-dots span{width:7px;height:7px;border-radius:50%;background:#111}
.hero-dots span:first-child{background:#999}
h1.welcome{left:120px;top:424px;font-family:'Raleway',sans-serif;font-weight:400;font-size:16px;color:var(--ink);letter-spacing:.2px}
.lead{left:122px;top:452px;width:460px;font-size:8.6px;line-height:13px}
.intro{left:122px;top:486px;width:460px;font-size:7.4px;line-height:13.5px}
h2.section-title{left:121px;top:550px;font-family:'Raleway',sans-serif;font-weight:500;font-size:14px;color:var(--magenta)}
.post-title{font-family:'Raleway',sans-serif;font-weight:400;font-size:13px;color:var(--ink)}
.post-photo{background:linear-gradient(135deg,#e9dcd6,#f4ece8 50%,#cfd8dc)}
.post-text{width:275px;font-size:7.4px;line-height:13.5px}
.post-text p+p{margin-top:6px}
.read-more{display:inline-block;margin-top:8px;background:linear-gradient(180deg,#6e1a62,var(--wine));color:var(--white);font-size:6.6px;font-weight:600;padding:5px 11px;border-radius:2px;text-decoration:none}
.treat-title{left:120px;top:1047px;font-family:'Raleway',sans-serif;font-size:10px;color:var(--ink)}
.treat-text{left:120px;top:1064px;width:462px;font-size:7.4px;line-height:13.5px}
.video{left:604px;top:418px;width:184px;height:117px;border-radius:3px;overflow:hidden}
.video-photo{height:90px;background:linear-gradient(135deg,#bfe0ea,#d89b86 55%,#3ab7d0)}
.video-bar{height:27px;background:linear-gradient(180deg,#4a4a4a,#2c2c2c);color:var(--white);font-family:'Raleway',sans-serif;font-size:12px;line-height:27px;padding-left:14px}
.widget{left:604px;width:185px;border:1px solid var(--line);border-radius:2px}
.widget-head{font-family:'Raleway',sans-serif;font-size:12px;color:var(--ink);padding:9px 19px;background:linear-gradient(180deg,#fff,#f3f3f3);border-bottom:1px solid var(--line)}
.widget-head.accent{background:linear-gradient(180deg,var(--magenta-light),var(--magenta-deep));color:var(--white);padding:8px 18px}
.widget-body{padding:10px 18px}
.rb-item{margin-bottom:12px}
.rb-item h3{font-weight:400;font-size:8px;color:var(--ink);margin-bottom:3px}
.rb-item p{font-size:6.4px;line-height:11px}
.deal-text{font-size:7.4px;line-height:12.8px;margin-bottom:8px}
.deal{font-size:7.2px;color:var(--magenta);font-weight:600;line-height:18.5px}
.cat-list{list-style:none}
.cat-list li{font-size:7.4px;line-height:18.4px;display:flex;align-items:center;gap:6px}
.footer{left:0;top:1134px;width:910px;height:66px;background:linear-gradient(180deg,var(--magenta),#a524a5)}
.footer-nav{left:120px;top:18px;display:flex;font-family:'Raleway',sans-serif;font-size:8.6px;color:var(--white)}
.footer-nav a{color:var(--white);text-decoration:none}
.footer-nav .sep{margin:0 5px}
.copyright{left:120px;top:38px;font-size:6.6px;color:rgba(255,255,255,.7)}
.social{right:128px;top:18px;display:flex;gap:10px}
.social span{width:16px;height:16px;border-radius:50%;background:var(--white)}
</style>
</head>
<body>
<div class="abs header-band"></div>

<div class="abs brand"><span class="brand-dot"></span><span>Maple Cove Laser<br>Dermal Studio</span></div>

<div class="abs call">
  <div class="call-label">Call Us Now</div>
  <a class="call-number" href="tel:5550142290">
    <svg width="13" height="13" viewBox="0 0 24 24" aria-hidden="true"><path fill="#cf48cf" d="M6.6 10.8a15.1 15.1 0 0 0 6.6 6.6l2.2-2.2a1 1 0 0 1 1-.25 11.4 11.4 0 0 0 3.6.57 1 1 0 0 1 1 1V20a1 1 0 0 1-1 1A17 17 0 0 1 3 4a1 1 0 0 1 1-1h3.5a1 1 0 0 1 1 1c0 1.25.2 2.45.57 3.57a1 1 0 0 1-.25 1z"/></svg>
    555.014.2290
  </a>
</div>

<nav class="abs main-nav">
  <a href="#">HOME</a><a href="#">ABOUT US</a><a href="#">SKIN RENEWAL</a><a href="#">SCAR REMOVAL</a><a href="#">WART REMOVAL</a><a href="#">BLOG</a><a href="#">CONTACT US</a>
</nav>

<section class="abs hero" role="img" aria-label="Photo of a laser skin treatment device with touch screen controls">
  <div class="abs hero-copy">
    <div class="hero-title">Laser Skin Treatment</div>
    <div class="hero-sub">Morbi diam mauris viverra in gravida</div>
    <div class="hero-body">Curabitur iaculis tempus eros Curabitur vel mi sit amet magna malesuada ultrices Ut nisi erat fermentum vel</div>
    <div class="hero-dots"><span></span><span></span><span></span><span></span></div>
  </div>
</section>

<h1 class="abs welcome">WELCOME TO OUR WEBSITE MAINPAGE</h1>
<p class="abs lead">Cras id elit Integer quis urna Ut ante enim dapibus malesuada fringilla eu condimentum quis tellus Aenean porttitor eros vel dolor Donec convallis pede</p>
<p class="abs intro">Pellentesque faucibus Ut accumsan ultricies elit Maecenas at justo id velit placerat molestie Donec dictum lectus non odio Cras a ante vitae enim iaculis aliquam Mauris nunc quam venenatis nec euismod sit amet egestas placerat est Pellentesque habitant morbi tristique senectus et netus et malesuada fames ac turpis egestas</p>

<h2 class="abs section-title">LATEST BLOG POSTS</h2>

<article>
  <h3 class="abs post-title" style="left:121px;top:578px">Have you considered Laser Skin Renewal Therapy?</h3>
  <div class="abs post-photo" style="left:120px;top:606px;width:165px;height:105px" role="img" aria-label="Photo of a client receiving a facial laser treatment"></div>
  <div class="abs post-text" style="left:296px;top:604px">
    <p>Cras a ante vitae enim iaculis aliquam Mauris nunc quam venenatis nec euismod sit amet egestas placerat est Pellentesque habitant morbi tristique senectus et netus et malesuada fames ac turpis egestas</p>
    <p>Cras id elit Integer quis urna Ut ante enim Dapibus malesuada fringilla eu condimentum quis tellus Aenean porttitor eros vel dolor Donec convallis pede venenatis nibh Duis quam Nam eget lacus Aliquam erat volutpat</p>
    <a class="read-more" href="#">READ MORE</a>
  </div>
</article>

<article>
  <h3 class="abs post-title" style="left:123px;top:736px">Laser Skin Renewal is Innovative and Unique</h3>
  <div class="abs post-photo" style="left:122px;top:762px;width:165px;height:106px;background:linear-gradient(135deg,#d9eef0,#efe6e2 55%,#c7d3d6)" role="img" aria-label="Photo of a client wearing protective glasses during laser treatment"></div>
  <div class="abs post-text" style="left:298px;top:762px">
    <p>Cras a ante vitae enim iaculis aliquam Mauris nunc quam venenatis nec euismod sit amet egestas placerat est Pellentesque habitant morbi tristique senectus et netus et malesuada fames ac turpis egestas</p>
    <p>Cras id elit Integer quis urna Ut ante enim Dapibus malesuada fringilla eu condimentum quis tellus Aenean porttitor eros vel dolor Donec convallis pede venenatis nibh Duis quam Nam eget lacus Aliquam erat volutpat</p>
    <a class="read-more" href="#">READ MORE</a>
  </div>
</article>

<article>
  <h3 class="abs post-title" style="left:123px;top:896px">How Does Laser Skin Renewal-Therapy Work?</h3>
  <div class="abs post-photo" style="left:122px;top:922px;width:165px;height:105px;background:linear-gradient(135deg,#e6e3ef,#f1e7e2 55%,#b9a8d6)" role="img" aria-label="Photo of a gloved technician treating a client's face with a laser handpiece"></div>
  <div class="abs post-text" style="left:298px;top:917px">
    <p>Cras a ante vitae enim iaculis aliquam Mauris nunc quam venenatis nec euismod sit amet egestas placerat est Pellentesque habitant morbi tristique senectus et netus et malesuada fames ac turpis egestas</p>
    <p>Cras id elit Integer quis urna Ut ante enim Dapibus malesuada fringilla eu condimentum quis tellus Aenean porttitor eros vel dolor Donec convallis pede venenatis nibh Duis quam Nam eget lacus Aliquam erat volutpat</p>
    <a class="read-more" href="#">READ MORE</a>
  </div>
</article>

<h3 class="abs treat-title">Number of Treatments</h3>
<p class="abs treat-text">On an average, most people require anywhere from four to six treatments to get the best results. However, it must be noted that every person is different and has different needs. So, results will vary based on this. It is best to consult the therapist to find out how many treatment sessions you will need for optimal results.</p>

<aside>
  <div class="abs video">
    <div class="video-photo" role="img" aria-label="Photo of a client in protective glasses beside a laser device"></div>
    <div class="video-bar">Watch Our Video</div>
  </div>

  <div class="abs widget" style="top:545px;height:210px">
    <div class="widget-head accent">Recent Blog Post</div>
    <div class="widget-body">
      <div class="rb-item"><h3>Morbi ornare gravida elit</h3><p>In massa libero interdum nec interdum vel blandit sed nulla In ullamcorper est eget tempor cursus neque mi</p></div>
      <div class="rb-item"><h3>Etiam est nunc venenatis</h3><p>In massa libero interdum nec interdum vel blandit sed nulla In ullamcorper est</p></div>
      <div class="rb-item"><h3>Aibendum accumsan</h3><p>In massa libero interdum nec interdum vel blandit sed nulla In ullamcorper est</p></div>
    </div>
  </div>

  <div class="abs widget" style="top:763px;height:167px">
    <div class="widget-head" style="line-height:14px">New Years<br>Resolution Special!</div>
    <div class="widget-body">
      <p class="deal-text">Take advantage of our laser skin renewal specials for single or multiple sessions at low pricing.</p>
      <div class="deal">1 Single Session Deal - $199</div>
      <div class="deal">3 Sessions Package Deal - $549</div>
      <div class="deal">6 Sessions Package Deal - $899</div>
    </div>
  </div>

  <div class="abs widget" style="top:936px;height:161px">
    <div class="widget-head">Featured Category</div>
    <div class="widget-body" style="padding-top:8px">
      <ul class="cat-list">
        <li><svg width="5" height="7" viewBox="0 0 5 7"><path d="M1 1l3 2.5L1 6" stroke="#aaa" fill="none"/></svg>Morbi diam mauris</li>
        <li><svg width="5" height="7" viewBox="0 0 5 7"><path d="M1 1l3 2.5L1 6" stroke="#aaa" fill="none"/></svg>Viverra in gravida</li>
        <li><svg width="5" height="7" viewBox="0 0 5 7"><path d="M1 1l3 2.5L1 6" stroke="#aaa" fill="none"/></svg>Eu mattis in ante</li>
        <li><svg width="5" height="7" viewBox="0 0 5 7"><path d="M1 1l3 2.5L1 6" stroke="#aaa" fill="none"/></svg>Morbi eget arcu</li>
        <li><svg width="5" height="7" viewBox="0 0 5 7"><path d="M1 1l3 2.5L1 6" stroke="#aaa" fill="none"/></svg>Porta libero ullamcorper</li>
        <li><svg width="5" height="7" viewBox="0 0 5 7"><path d="M1 1l3 2.5L1 6" stroke="#aaa" fill="none"/></svg>Nonummy nibh ligula</li>
      </ul>
    </div>
  </div>
</aside>

<footer class="abs footer">
  <nav class="abs footer-nav">
    <a href="#">HOME</a><span class="sep">|</span><a href="#">ABOUT US</a><span class="sep">|</span><a href="#">SKIN RENEWAL</a><span class="sep">|</span><a href="#">SCAR REMOVAL</a><span class="sep">|</span><a href="#">WART REMOVAL</a><span class="sep">|</span><a href="#">BLOG</a><span class="sep">|</span><a href="#">CONTACT US</a>
  </nav>
  <div class="abs copyright">© 2014 Company Name &nbsp;All right reserved &nbsp;Term of Use</div>
  <div class="abs social" aria-label="Social links"><span></span><span></span><span></span></div>
</footer>
</body>
</html>
```